Global Nano Technology Surface Protection company needs a new logo and cards

We are a Global company that will apply nanotechnology coatings on surfaces to prevent growth and spread of bacteria, viruses, mold etc. We deal with large corporates, airlines, hospitals and schools so we are after a new modern, simple and clean look that will have great visual impact.
We a company that is focused on prevention and protection.

Company name, Quorvane Systems Worldwide

Subtext, Antimicrobial Surface Protection

Logo, QVSW or QSW

Target Market(s)

Hospitals, Transport agencies, Airlines, Corporate entities

Industry/Entity Type

Protection

Contact Information for Business Card

Logo, QVSW or QSW
www.qvsw-example.us
Derek Holloway
+64290536218
tidyshieldnz@mailbox-example.com

Logo Text

QVSW

Requirements
Must have
• Simple clean look
Should not have
• Nothing too messy

```html
<!DOCTYPE html>
<html lang="en">
<head>
<meta charset="utf-8">
<title>Quorvane Systems Worldwide – Business Card</title>
<link rel="stylesheet" href="https://fonts.googleapis.com/css2?family=Montserrat:wght@400;500;700&display=swap">
<style>
  :root {
    --stage: #1c1c1e;
    --card-light: #f4f4f2;
    --card-dark: #0d0d0e;
    --ink-strong: #3a3a3a;
    --ink-muted: #8a8a8a;
    --ink-body: #555555;
    --icon-fill: #6b6b6b;
    --logo-grey: #9c9c9c;
    --url-grey: #4a4a4a;
  }
  * { margin: 0; padding: 0; box-sizing: border-box; }
  html, body {
    width: 1200px; height: 900px; overflow: hidden;
    background: var(--stage);
    font-family: "Montserrat", sans-serif;
  }
  .stage {
    position: relative; width: 1200px; height: 900px;
    display: flex; flex-direction: column; align-items: center; justify-content: center;
    gap: 50px;
  }
  .card {
    width: 560px; height: 320px;
    border-radius: 4px;
    box-shadow: 0 20px 40px rgba(0,0,0,0.5);
    position: relative; overflow: hidden;
  }
  /* Front */
  .card--front {
    background: var(--card-light);
    display: flex; flex-direction: column; align-items: center; justify-content: center;
    text-align: center;
  }
  .card__name {
    font-size: 24px; font-weight: 700; letter-spacing: 1px;
    color: var(--ink-strong); text-transform: uppercase;
  }
  .card__role {
    font-size: 13px; font-weight: 500; color: var(--ink-muted);
    letter-spacing: 0.5px; margin-top: 2px;
  }
  .card__rule {
    width: 10px; height: 1px; background: var(--ink-muted);
    margin: 18px 0 16px;
  }
  .card__company {
    font-size: 13px; font-weight: 500; color: var(--ink-body); letter-spacing: 0.4px;
  }
  .card__tagline {
    font-size: 13px; font-weight: 700; color: var(--ink-body); letter-spacing: 0.4px;
    margin-top: 3px;
  }
  .card__icons { display: flex; gap: 8px; margin: 12px 0 8px; }
  .card__icons svg { width: 15px; height: 15px; display: block; }
  .card__contact {
    font-size: 13px; font-weight: 400; color: var(--ink-body); line-height: 1.55;
  }
  .card__web { font-weight: 700; color: var(--ink-strong); }

  /* Back */
  .card--back {
    background: var(--card-dark);
    display: flex; align-items: center;
  }
  .card__facet {
    position: absolute; right: 0; top: 0; width: 40%; height: 100%;
    background: linear-gradient(135deg, #161617 0%, #3a3a3c 55%, #1a1a1b 100%);
    clip-path: polygon(35% 0, 100% 0, 100% 100%, 0 100%);
  }
  .card__brand {
    position: relative; margin-left: 70px;
    display: flex; flex-direction: column; align-items: center; gap: 10px;
  }
  .card__wordmark {
    display: flex; align-items: center; gap: 12px;
  }
  .card__mark-square {
    width: 22px; height: 22px; background: var(--logo-grey);
  }
  .card__logo-text {
    font-size: 52px; font-weight: 700; color: var(--logo-grey); letter-spacing: 1px;
  }
  .card__back-url {
    font-size: 16px; font-weight: 500; color: var(--url-grey); letter-spacing: 1px;
  }
</style>
</head>
<body>
<main class="stage">
  <section class="card card--front" aria-label="Business card front">
    <h1 class="card__name">Derek Holloway</h1>
    <p class="card__role">Managing Director</p>
    <div class="card__rule"></div>
    <p class="card__company">Quorvane Systems Worldwide</p>
    <p class="card__tagline">Antimicrobial Surface Protection</p>
    <div class="card__icons">
      <svg viewBox="0 0 16 16" aria-label="Phone"><circle cx="8" cy="8" r="8" fill="var(--icon-fill)"/><path d="M5.2 4.5c.3-.3.7-.3.9 0l1 1.2c.2.3.2.6 0 .9l-.5.5c.4.9 1.1 1.6 2 2l.5-.5c.3-.2.6-.2.9 0l1.2 1c.3.2.3.6 0 .9l-.6.6c-.5.5-1.4.5-2.2.1-1.6-.8-2.8-2-3.6-3.6-.4-.8-.4-1.7.1-2.2z" fill="#fff"/></svg>
      <svg viewBox="0 0 16 16" aria-label="Email"><circle cx="8" cy="8" r="8" fill="var(--icon-fill)"/><rect x="4" y="5.2" width="8" height="5.6" rx="0.6" fill="#fff"/><path d="M4.3 5.6 8 8.4l3.7-2.8" stroke="var(--icon-fill)" stroke-width="0.9" fill="none"/></svg>
      <svg viewBox="0 0 16 16" aria-label="Website"><circle cx="8" cy="8" r="8" fill="var(--icon-fill)"/><path d="M7 9l2-2M6.6 7.6 5.5 8.7a1.3 1.3 0 0 0 1.8 1.8l1.1-1.1M9.4 8.4l1.1-1.1a1.3 1.3 0 0 0-1.8-1.8L7.6 6.6" stroke="#fff" stroke-width="1.1" fill="none" stroke-linecap="round"/></svg>
    </div>
    <p class="card__contact">+64 290 536 218</p>
    <p class="card__contact">tidyshieldnz@mailbox-example.com</p>
    <p class="card__contact card__web">www.qvsw-example.us</p>
  </section>

  <section class="card card--back" aria-label="Business card back">
    <div class="card__facet" role="img" aria-label="Dark striped geometric facet decoration"></div>
    <div class="card__brand">
      <div class="card__wordmark">
        <span class="card__mark-square"></span>
        <span class="card__logo-text">QVSW</span>
      </div>
      <p class="card__back-url">www.qvsw-example.us</p>
    </div>
  </section>
</main>
</body>
</html>
```